Bright Forge Iron Client Handout

We need a cover sheet for our processes flyer that we will be handing out to our clients. Attached is a set of stairs that our company has erected, as well as our logos and a rough draft of what we are looking for. We would like the stairs in our image to be sharpened if at all possible, taken out from the background, and instead placed atop an image of a beautiful Arizona sunset/landscape. We would like the text to be editable and we would like to retain the rights to the product, as our language on this project is still being revised. We would also like the placement/positioning of our logos to be refined to look more modernized and professional.

Target Market(s)

Construction contractors, vendors and prospective builders.

Industry/Entity Type

Structural Steel

Requirements
Must have
• • clean up the background
• see if the stair image could be sharpened at all
• Put a beautiful AZ sunset behind it
• Refine location/layout of the BFI logo & header up top to make it a modernized, professional handout that we can give to clients
• NOTE: we may have a small amount of refining of the language used on the sub bullets so want to make sure we have the rights to the document to edit and revise it
Nice to have
• Please use our logo on this.
We would like a very Arizona-esque looking background. See link below for examples

https://www.examplefind.test/search?q=arizona+sunset&rlz=1X2YZAB_enUS100US100&sxsrf=QWeRt02abCDefGHijKLmnOPqrST5Uv:1500000000000&source=lnms&tbm=isch&sa=X&ved=3bcDEfghIjKlmNoPqRsTuVwXyZ0Q_BcDeFgHiJkLmNoPqRs&biw=1920&bih=969

```html
<!DOCTYPE html>
<html lang="en">
<head>
<meta charset="utf-8">
<title>Bright Forge Iron – Iron-Strong Stairway to Success</title>
<link rel="stylesheet" href="https://fonts.googleapis.com/css2?family=Saira+Stencil+One&family=Michroma&family=Barlow:wght@400;500&display=swap">
<style>
  :root {
    --page-bg: #e9f0f7;
    --sky-top: #3d403f;
    --sky-mid: #8f9292;
    --sky-light: #e4e4e2;
    --sunset: #e8d8bd;
    --dune: #9c8a7f;
    --ground: #8c8c8e;
    --red: #e21d22;
    --red-dark: #8e0f12;
    --ink: #1e1e1e;
    --white: #ffffff;
    --steel-light: #e9eef2;
    --steel-mid: #8fa0ad;
    --steel-dark: #4c5962;
  }
  * { box-sizing: border-box; margin: 0; padding: 0; }
  html, body {
    width: 1200px; height: 1200px; overflow: hidden;
    background: var(--page-bg);
  }
  .flyer {
    position: absolute; left: 136px; top: 0;
    width: 927px; height: 1200px; overflow: hidden;
    font-family: "Barlow", Arial, sans-serif;
    color: var(--ink);
  }
  .backdrop {
    position: absolute; inset: 0;
    background:
      radial-gradient(ellipse 55% 30% at 55% 25%, rgba(235,235,232,.9), rgba(235,235,232,0) 70%),
      linear-gradient(to bottom,
        var(--sky-top) 0%, var(--sky-mid) 22%, var(--sky-light) 45%,
        var(--sky-light) 70%, var(--sunset) 80%, var(--dune) 86%,
        var(--ground) 90%, #a3a3a5 100%);
  }
  .stair-photo {
    position: absolute; left: 292px; top: 228px;
    width: 396px; height: 830px;
    background: linear-gradient(to bottom, rgba(70,70,72,.55), rgba(90,90,92,.35) 60%, rgba(80,80,82,.5));
  }
  .brand-panel {
    position: absolute; left: 0; top: 43px;
    width: 295px; height: 178px;
    background: linear-gradient(135deg, #f3f6f8 0%, #c9d2d7 55%, #eef3f6 100%);
    clip-path: polygon(0 0, 100% 0, 86% 100%, 0 100%);
    display: flex; align-items: center; justify-content: center;
    padding-right: 30px;
  }
  .brand-name {
    font-family: "Barlow", Arial, sans-serif;
    font-weight: 500; font-size: 26px; letter-spacing: -0.5px;
    color: #2b2b2b;
  }
  .title {
    position: absolute; left: 372px; top: 56px;
    font-family: "Saira Stencil One", Impact, sans-serif;
    font-size: 92px; line-height: 92px; letter-spacing: 1px;
    white-space: nowrap;
    background: linear-gradient(to bottom, var(--steel-light) 0%, var(--steel-mid) 45%, var(--steel-dark) 55%, var(--steel-light) 100%);
    -webkit-background-clip: text; background-clip: text; color: transparent;
    transform: scaleX(0.82); transform-origin: left top;
  }
  .subtitle {
    position: absolute; left: 372px; top: 155px;
    width: 507px; height: 45px;
    background: #1c1c1c; border: 1px solid #555;
    display: flex; align-items: center; justify-content: center;
    font-family: "Michroma", sans-serif; font-size: 19px;
    letter-spacing: 3px; color: #d9dde0; white-space: nowrap;
  }
  .step { position: absolute; }
  .step--left { left: 39px; width: 240px; }
  .step--right { left: 701px; width: 205px; }
  .step-label {
    display: block; width: 187px; height: 29px; line-height: 29px;
    padding-left: 12px; white-space: nowrap;
    font-family: "Michroma", sans-serif; font-size: 12px; font-weight: 400;
    letter-spacing: 2px;
    color: var(--white);
    background: linear-gradient(to right, var(--red-dark), var(--red));
    clip-path: polygon(0 0, 93% 0, 100% 100%, 0 100%);
  }
  .step--wide { width: 380px; }
  .step--wide .step-label { width: 372px; clip-path: polygon(0 0, 96% 0, 100% 100%, 0 100%); }
  .step-points { list-style: none; margin-top: 10px; padding-left: 12px; }
  .step-points li {
    font-size: 13px; line-height: 16.3px; margin-bottom: 8px;
    padding-left: 10px; text-indent: -10px; white-space: nowrap;
  }
  .step-points li::before { content: "• "; }
</style>
</head>
<body>
  <article class="flyer">
    <div class="backdrop" role="img" aria-label="Arizona desert sunset landscape with dunes under a cloudy sky"></div>
    <div class="stair-photo" role="img" aria-label="Erected multi-level steel stair tower with railings"></div>

    <header>
      <div class="brand-panel"><span class="brand-name">Bright Forge Iron</span></div>
      <h1 class="title">IRON-STRONG</h1>
      <p class="subtitle">STAIRWAY TO SUCCESS</p>
    </header>

    <section class="step step--left" style="top:325px;">
      <h2 class="step-label">EVALUATE</h2>
      <ul class="step-points">
        <li>Post Project Assessment</li>
        <li>Net Promoter Score</li>
      </ul>
    </section>

    <section class="step step--left" style="top:571px;">
      <h2 class="step-label">IMPLEMENT</h2>
      <ul class="step-points">
        <li>Contact During Fabrication<br>(75% Completed Before We Shop Up)</li>
        <li>3D Models Provided</li>
      </ul>
    </section>

    <section class="step step--left" style="top:829px;">
      <h2 class="step-label">COLLABORATE</h2>
      <ul class="step-points">
        <li>Pre-Construction Value<br>Engineering</li>
        <li>Budgeting Assistance</li>
      </ul>
    </section>

    <section class="step step--left step--wide" style="top:1070px;">
      <h2 class="step-label">IRON STRONG RELATIONSHIPS</h2>
      <ul class="step-points">
        <li>Prior Success Foundation</li>
        <li>Zippered Relationships</li>
      </ul>
    </section>

    <section class="step step--right" style="top:466px;">
      <h2 class="step-label">DELIVER</h2>
      <ul class="step-points">
        <li>Safely erect steel</li>
        <li>Blink and We Are Done</li>
      </ul>
    </section>

    <section class="step step--right" style="top:707px;">
      <h2 class="step-label">STRATEGIZE</h2>
      <ul class="step-points">
        <li>Iron-Strong Expectations<br>Meeting</li>
        <li>Smarter, Faster, Better<br>(Coordinate to Maximize<br>Prefabrication)</li>
      </ul>
    </section>

    <section class="step step--right" style="top:918px;">
      <h2 class="step-label">DISCOVER</h2>
      <ul class="step-points">
        <li>Share our Steel Expertise<br>(Best Practices)</li>
        <li>Identify Best Value<br>Opportunities (What’s Best<br>for the Project)</li>
      </ul>
    </section>
  </article>
</body>
</html>
```